Kestrel Summit 2019 Enemies of the End-Times Church Flyer

We want a church conference flyer designed. We are looking for a professional, yet catchy design that uses our brand colors and logo creatively while communicating key information of the event effectively. <br/>The flyer must include all of the following:<br/>Title: Kestrel Summit 2019<br/>Topic: The Enemies of The End-Times Church <br/>Subtitles: <br/> -How the antichrist raises an army by social behavior engineering. <br/>-How the architects of modern social constructs escaped the church's radar. <br/>-The Holy Spirit's end-times agenda:<br/> The Knock-Out Punch!<br/>Speaker: Prophet Marcus Toliver <br/>Dates/time: December 27, 28 & 29 at 6pm<br/>Location: Halvorn Community Center <br/> 241 Pellham Street <br/> Portland, ME 04102<br/>Contact info: phone: 207-555-0148 <br/>email: contact@brookmeadow.example <br/> www.vutel.example<br/>*The flyer must also include a picture of the speaker and our Vutel logo <br/>Thanks, we look forward to seeing what you come up with!

Colors

Designer to choose colors to be used in the design.

Requirements
Must have
• The flyer must include all of the following:
• Title: Kestrel Summit 2019
• Topic: The Enemies of The End-Times Church
• Subtitles:
• -How the antichrist raises an army by social behavior engineering.
• -How the architects of modern social constructs escaped the church's radar.
• -The Holy Spirit's end-times agenda:
• The Knock-Out Punch!
• Speaker: Prophet Marcus Toliver
• Dates/time: December 27, 28 & 29 at 6pm
• Location: Halvorn Community Center
• 241 Pellham Street
• Portland, ME 04102
• Contact info: phone: 207-555-0148
• email: contact@brookmeadow.example
• www.vutel.example
• *The flyer must also include a picture of the speaker and our Vutel logo
Should not have
• Pictures of crosses or church buildings

```html
<!DOCTYPE html>
<html lang="en">
<head>
<meta charset="utf-8">
<title>Kestrel Summit 2019 – Flyer</title>
<link rel="stylesheet" href="https://fonts.googleapis.com/css2?family=Anton&family=Fira+Sans+Condensed:wght@500;600;700&family=Fjalla+One&family=Tinos:wght@700&display=swap">
<style>
  :root {
    --navy: #3b5877;
    --navy-deep: #2f4a66;
    --orange: #f7a443;
    --orange-soft: #f9b866;
    --paper: #ffffff;
    --stage: #ecebef;
    --ink: #3b5877;
  }
  html, body {
    margin: 0; padding: 0;
    width: 1200px; height: 1037px;
    overflow: hidden;
    background: var(--stage);
  }
  .flyer {
    position: absolute;
    left: 210px; top: 16px;
    width: 780px; height: 1005px;
    background: var(--paper);
    overflow: hidden;
    box-shadow: 0 6px 24px rgba(0,0,0,.18);
    font-family: "Fira Sans Condensed", sans-serif;
    color: var(--ink);
  }
  .flyer > * { position: absolute; }
  .backdrop, .speaker-photo { left: 0; top: 0; width: 780px; height: 1005px; }
  .title { left: 0; top: 0; width: 780px; height: 250px; }
  .edition {
    left: 34px; top: 238px; margin: 0;
    font-family: "Anton", sans-serif; font-weight: 400;
    font-size: 68px; line-height: 1; letter-spacing: 1px;
  }
  .edition .word { color: var(--orange); }
  .edition .year { color: var(--navy); margin-left: 14px; }
  .topic {
    left: 48px; top: 350px; margin: 0;
    padding-left: 14px;
    border-left: 3px solid var(--orange);
    font-family: "Fjalla One", sans-serif; font-weight: 400;
    font-size: 36px; line-height: 1.08; color: var(--navy);
    text-transform: uppercase;
  }
  .topic .accent { color: var(--orange); }
  .topic .line2 { display: block; padding-left: 8px; }
  .points {
    left: 66px; top: 462px; width: 360px;
    margin: 0; padding: 0; list-style: none;
    font-size: 17px; font-weight: 600; line-height: 1.2;
    border-left: 3px solid var(--orange);
    padding-left: 10px;
  }
  .points li { margin-bottom: 12px; padding-left: 14px; text-indent: -12px; }
  .points li::before { content: "•"; margin-right: 6px; }
  .knockout { left: 440px; top: 480px; width: 220px; height: 220px; }
  .dates {
    left: 96px; top: 650px; width: 240px; height: 66px;
    border-radius: 33px;
    background: linear-gradient(180deg, var(--orange-soft), var(--orange));
    text-align: center; color: var(--paper);
    font-family: "Fjalla One", sans-serif; font-size: 24px; line-height: 1.15;
    padding-top: 4px; box-sizing: border-box;
  }
  .dates .time { color: var(--navy); }
  .venue { left: 66px; top: 732px; width: 310px; text-align: center; }
  .venue svg { display: block; margin: 0 auto 4px; }
  .venue .name {
    font-family: "Fjalla One", sans-serif; font-size: 23px; color: var(--navy);
    display: inline-block; padding: 0 6px; position: relative;
  }
  .venue .address {
    font-family: Arial, Helvetica, sans-serif; font-size: 13px; color: var(--navy);
    border: 1px solid var(--orange); border-top: none;
    margin-top: -10px; padding: 12px 6px 2px;
  }
  .brand {
    left: 70px; top: 842px; display: flex; align-items: center; gap: 10px;
    font-family: "Fira Sans Condensed", sans-serif; font-weight: 600;
    font-size: 46px; letter-spacing: 2px; color: var(--navy);
  }
  .brand .dot { width: 16px; height: 16px; border-radius: 50%; background: var(--orange); }
  .contact { left: 70px; top: 906px; margin: 0; padding: 0; list-style: none; }
  .contact li { display: flex; align-items: center; gap: 8px; font-family: Arial, Helvetica, sans-serif; font-size: 14px; color: var(--navy); }
  .contact .phone { font-family: "Fira Sans Condensed", sans-serif; font-weight: 700; font-size: 36px; line-height: 1.05; }
  .speaker {
    left: 418px; top: 842px; width: 362px; height: 76px;
    background: rgba(47,74,102,.88);
    font-family: "Tinos", serif; font-weight: 700;
    padding: 6px 0 0 38px; box-sizing: border-box; line-height: 1.05;
  }
  .speaker .label { display: block; color: var(--orange); font-size: 22px; }
  .speaker .name { display: block; color: var(--paper); font-size: 30px; }
</style>
</head>
<body>
<main class="flyer">
  <svg class="backdrop" viewBox="0 0 780 1005" aria-hidden="true">
    <path d="M470 55 L780 55 L780 1005 L520 1005 C420 930 370 820 395 700 C415 610 480 560 520 450 C490 520 470 560 450 440 C440 300 470 180 470 55 Z" fill="var(--orange)"/>
  </svg>

  <svg class="title" viewBox="0 0 780 250" aria-label="Kestrel">
    <text x="22" y="232" textLength="740" lengthAdjust="spacingAndGlyphs" font-family="Anton, sans-serif" font-size="236" fill="var(--navy)">KESTREL</text>
  </svg>

  <svg class="speaker-photo" viewBox="0 0 780 1005">
    <defs>
      <linearGradient id="photoTone" x1="0" y1="0" x2="0" y2="1">
        <stop offset="0" stop-color="#5a5654"/>
        <stop offset="0.35" stop-color="#8a3a3c"/>
        <stop offset="1" stop-color="#3c3f46"/>
      </linearGradient>
    </defs>
    <path role="img" aria-label="Photo of the speaker, Prophet Marcus Toliver, seated in a grey jacket over a red sweater"
      d="M600 270 C660 270 700 320 700 380 C700 420 690 440 740 470 C780 500 780 560 780 600 L780 1005 L455 1005 C450 900 470 760 500 620 C520 520 560 470 560 440 C540 400 535 330 560 300 C570 285 585 270 600 270 Z"
      fill="url(#photoTone)"/>
  </svg>

  <h2 class="edition"><span class="word">SUMMIT</span><span class="year">2019</span></h2>

  <h1 class="topic">The Enemies<span class="line2">of the <span class="accent">End-Times Church</span></span></h1>

  <ul class="points">
    <li>How the antichrist raises an army by social behavior engineering.</li>
    <li>How the architects of modern social constructs escaped the church's radar.</li>
    <li>The Holy Spirit's end-times agenda:</li>
  </ul>

  <svg class="knockout" viewBox="0 0 220 220" aria-label="The Knock-Out Punch!">
    <polygon fill="var(--navy-deep)" points="110,4 128,62 178,18 160,80 216,82 168,112 212,160 150,146 148,214 112,160 70,212 72,148 8,170 52,118 2,76 66,78 48,20 96,62"/>
    <g transform="rotate(-18 110 112)" font-family="Fjalla One, sans-serif" text-anchor="middle">
      <text x="110" y="92" font-size="24" fill="var(--paper)">The</text>
      <text x="110" y="120" font-size="26" fill="var(--orange)">Knock-Out</text>
      <text x="110" y="148" font-size="24" fill="var(--paper)">Punch !</text>
    </g>
  </svg>

  <div class="dates">December<br><span>27, 28 &amp; 29</span> <span class="time">at</span> 6pm</div>

  <address class="venue" style="font-style:normal">
    <svg width="22" height="30" viewBox="0 0 22 30" aria-hidden="true">
      <path d="M11 1 C5 1 1 5.5 1 11 C1 18 11 29 11 29 C11 29 21 18 21 11 C21 5.5 17 1 11 1 Z" fill="var(--navy)"/>
      <circle cx="11" cy="11" r="4" fill="var(--paper)"/>
    </svg>
    <span class="name">Halvorn Community Center</span>
    <div class="address">241 Pellham Street Portland, ME 04102</div>
  </address>

  <div class="brand"><span class="dot"></span>VUTEL</div>

  <ul class="contact">
    <li class="phone">
      <svg width="24" height="24" viewBox="0 0 24 24" aria-hidden="true"><circle cx="12" cy="12" r="11" fill="none" stroke="var(--orange)" stroke-width="2"/><path d="M8 6 L10 6 L11 9 L9.5 10.5 C10.3 12.2 11.8 13.7 13.5 14.5 L15 13 L18 14 L18 16 C18 17 17 18 16 18 C10.5 18 6 13.5 6 8 C6 7 7 6 8 6 Z" fill="var(--navy)"/></svg>
      207-555-0148
    </li>
    <li>
      <svg width="16" height="16" viewBox="0 0 16 16" aria-hidden="true"><circle cx="8" cy="8" r="8" fill="var(--orange)"/><rect x="4" y="5" width="8" height="6" fill="none" stroke="#fff" stroke-width="1"/><path d="M4 5 L8 8.5 L12 5" fill="none" stroke="#fff" stroke-width="1"/></svg>
      contact@brookmeadow.example
    </li>
    <li>
      <svg width="16" height="16" viewBox="0 0 16 16" aria-hidden="true"><circle cx="8" cy="8" r="8" fill="var(--orange)"/><circle cx="8" cy="8" r="4.5" fill="none" stroke="#fff" stroke-width="1"/><path d="M3.5 8 H12.5 M8 3.5 V12.5" stroke="#fff" stroke-width="1"/></svg>
      www.vutel.example
    </li>
  </ul>

  <div class="speaker"><span class="label">Speaker:</span><span class="name">Prophet Marcus Toliver</span></div>
</main>
</body>
</html>
```